Web design for our new company

We need a web design for our product and for our company.
And the main is our Product tool called "velmora".
----------------------------------------------------------
[Our company's Goal]
Make organization’s communication smooth and healthy with transparency and efficiency for works and tasks in all levels with our workflow tool.

[Our Mission]
Our mission is to achieve business goals with customers.
We work together to identify the goals for your company, guides your strategy and bring the technology answers which best fit to achieve the goals.

[What we do]
We have a workflow tool "velmora"
- Very simple end-user configurable workflow for any company processes
(Targeting small-med size company)
- Graphical & fun features for startup users
- Simple and easy task control with quillbox e-mail look & feel
- Non charged skill up guidance
- Additional features with;
Multiple delegation
Clear status for each owner
Task owner management console with due date reminders&reporting

Others
1. System Development & Implementation Service
Our client list includes a wide variety of small to medium to major sized enterprises.
We can offer from full-scratch based development to packaged system implementation.

2. Project Management(PM) Service
We will provide end-to-end PM service with experienced PM.
Our service is not only “managing” but “leading” to bring success to achieve the goal.

3.Consultation Service

Consulting services to a wide range of fields such as creating business strategy, business process Kaizen, IT system consultation and change management.

Target Market(s)

Business to Business
Mainly to medium size - startup company

Industry/Entity Type

It Company

Coding

Coded - Design and coding required

Number of Pages Required

5+ page

Colors
0255a3
33a6d7
86cfc6
33b8a4
add136
cadf82
fbf289
fee18a
faa54b

Requirements
Must have
• We need Pages for
• Company mission
• Service Overview
• Contact
• Privacy Policy
• Terms and Conditions
• =========================
• As there were some questions, I add followings.---------
• 1. File Format
• We are going to use Brixel cloud services to upload finished web files.
• The finished files should be ready to use by simply replacing images and text.
• Please provide me "easy to handle" template with "sophisticated design".
• Thanks!
• 2. Multiple Languages
• We need buttons for changing language.
• We will have this translated to German, English and Japanese.
• Thank you so much!!
Nice to have
• These are current Logos and will be a next project to revise them...
• Attached Company Profile and Logo design
• 1. Company Profile
• 2. Our Company Logo
• 3. Our Product Logo -> This is most close to our image of design base.
• 4. Product Logo for PPT Header
• All just for your reference.
• ---------
• As there were some request, I added attachment as for contents for Our mission page.
Should not have
• I hope to see some unique designs.
• (Sorry please ignore my last update as I checked with our CEO.
• Bootstrap is absolutely good template.)

```html
<!DOCTYPE html>
<html lang="en">
<head>
<meta charset="utf-8">
<title>Corvane — Best System Development Services</title>
<link rel="stylesheet" href="https://fonts.googleapis.com/css2?family=Work+Sans:wght@300;400;500;600&display=swap">
<style>
:root{
  --green:#8aa21c;
  --green-dark:#6b7d12;
  --ink:#2f2f2f;
  --text:#555;
  --hero-bg:#eef4f3;
  --band:#e2ecea;
  --gray-bg:#f4f4f4;
  --card:#ffffff;
  --yellow:#fbd86a;
  --blue:#33a6d7;
  --navy:#0255a3;
  --teal:#86cfc6;
  --sea:#33b8a4;
  --orange:#faa54b;
  --footer-bar:#2b2b2b;
}
*{box-sizing:border-box;margin:0;padding:0}
html,body{width:1200px;height:3273px;overflow:hidden}
body{position:relative;font-family:"Work Sans",sans-serif;color:var(--text);background:#fff}
.art{position:absolute;border-radius:14px}
h2{font-weight:500;color:var(--ink);letter-spacing:.5px}
h2 span{color:var(--green)}

/* header & hero */
.hero{position:absolute;left:0;top:0;width:1200px;height:700px;background:var(--hero-bg);overflow:hidden}
.band{position:absolute;height:34px;border-radius:17px;background:var(--band)}
.brand{position:absolute;left:84px;top:30px;display:flex;align-items:center;gap:10px;font-size:24px;font-weight:500;color:var(--green)}
.brand i{width:30px;height:30px;border-radius:50%;border:3px solid var(--green);display:block}
.nav{position:absolute;top:50px;left:0;width:1200px;font-size:15px;color:var(--ink)}
.nav a{position:absolute;color:inherit;text-decoration:none}
.lang{position:absolute;right:87px;top:12px;display:flex;gap:0;font-size:11.5px;font-weight:500;border:1px solid #c9d3d1;border-radius:12px;overflow:hidden;background:#fff}
.lang span{padding:3px 10px;color:var(--ink)}
.lang span.on{background:var(--green);color:#fff}
.hero-title{position:absolute;left:84px;top:250px;font-weight:300;font-size:41px;line-height:48px;color:var(--ink)}
.hero-title span{display:block;color:var(--green);font-weight:400;letter-spacing:.5px}
.hero-text{position:absolute;left:87px;top:352px;width:480px;font-size:13px;line-height:20px;color:#6a6a6a}
.watch{position:absolute;left:87px;top:404px;display:flex;align-items:center;gap:8px;font-size:13.5px;font-weight:600;color:var(--green-dark)}

/* about */
.about{position:absolute;left:85px;top:556px;width:1030px;height:386px;background:var(--card);box-shadow:0 4px 14px rgba(0,0,0,.16)}
.about .frame{position:absolute;left:28px;top:30px;width:340px;height:320px;border:7px solid var(--yellow);border-right:none;border-bottom:none}
.about .frame2{position:absolute;left:361px;top:110px;width:8px;height:240px;background:var(--yellow)}
.about h2{position:absolute;left:440px;top:34px;font-size:36px}
.about p{position:absolute;left:440px;top:96px;width:540px;font-size:13px;line-height:22px}
.btn-outline{position:absolute;left:440px;top:200px;width:150px;height:26px;border:1px solid #888;font-size:12px;color:var(--green-dark);text-align:center;line-height:24px}
.thumb{position:absolute;top:259px;width:172px;height:100px}
.slider-arrow{position:absolute;top:296px;width:16px;height:24px;background:var(--green);color:#fff;font-size:13px;text-align:center;line-height:24px}

/* goal & mission */
.goal h2,.mission h2{position:absolute;font-size:33px}
.block-text{position:absolute;font-size:13px;line-height:22px}
.divider{position:absolute;left:87px;top:1258px;width:1026px;height:1px;background:#e8e8e8}

/* what we do */
.services{position:absolute;left:0;top:1559px;width:1200px;height:1417px;background:var(--gray-bg)}
.services>h2{position:absolute;left:0;top:52px;width:1200px;text-align:center;font-size:34px}
.card{position:absolute;left:87px;width:1026px;background:var(--card);box-shadow:0 3px 10px rgba(0,0,0,.14)}
.svc-icon{position:absolute;width:62px;height:62px;border-radius:50%;background:var(--green);border:4px solid #dfe8bd}
.svc-title{position:absolute;font-size:21px;font-weight:500;letter-spacing:1.5px;line-height:26px;color:var(--green)}
.svc-text{position:absolute;font-size:12.5px;line-height:20px;color:#444}
.ticks{position:absolute;list-style:none;font-size:12.5px;line-height:17px;color:#444}
.ticks li{position:relative;padding-left:20px;margin-bottom:8px}
.ticks li::before{content:"»";position:absolute;left:0;color:var(--green)}

/* footer */
.footer{position:absolute;left:0;top:2976px;width:1200px;height:246px;background:var(--green-dark);color:#fff}
.footer h3{position:absolute;font-size:14.5px;font-weight:600;letter-spacing:.5px}
.info{position:absolute;left:87px;display:flex;gap:12px;font-size:13.5px;line-height:21px;width:220px}
.info svg{flex:none;margin-top:3px}
.vline{position:absolute;left:392px;top:30px;width:1px;height:190px;background:rgba(255,255,255,.55)}
.field{position:absolute;font-size:12px;border-bottom:1px solid rgba(255,255,255,.8);padding-bottom:4px}
.send{position:absolute;left:497px;top:207px;width:104px;height:26px;border:1px solid #fff;font-size:11px;text-align:center;line-height:24px}
.copyright{position:absolute;left:0;top:3222px;width:1200px;height:51px;background:var(--footer-bar);color:#fff;font-size:13px;text-align:center;line-height:51px}
</style>
</head>
<body>

<header class="hero">
  <div class="band" style="left:-40px;top:130px;width:420px"></div>
  <div class="band" style="left:0;top:500px;width:390px"></div>
  <div class="band" style="left:130px;top:560px;width:360px"></div>
  <div class="band" style="left:900px;top:520px;width:340px"></div>
  <div class="band" style="left:-60px;top:630px;width:300px"></div>
  <div class="band" style="left:720px;top:610px;width:420px"></div>

  <div class="brand"><i></i>Corvane</div>
  <div class="lang" aria-label="Language"><span class="on">EN</span><span>DE</span><span>JA</span></div>
  <nav class="nav">
    <a style="left:438px">Home</a>
    <a style="left:566px">About Us</a>
    <a style="left:718px">Product Overview</a>
    <a style="left:934px">Pricing</a>
    <a style="left:1067px">Policy</a>
  </nav>

  <h1 class="hero-title">Best System<span>Development Services</span></h1>
  <p class="hero-text">Lorem Ipsum is simply dummy text of the printing and typesetting industry. Lorem Ipsum has been the industry's standard dummy text</p>
  <div class="watch">
    <svg width="22" height="22" viewBox="0 0 22 22"><circle cx="11" cy="11" r="9.5" fill="none" stroke="#6b7d12" stroke-width="2"/><path d="M9 7l6 4-6 4z" fill="#6b7d12"/></svg>
    Watch Our Video
  </div>
  <div class="art" role="img" aria-label="Illustration of desktop, laptop, tablet and phone surrounded by web and app icons" style="left:622px;top:164px;width:490px;height:326px;background:linear-gradient(135deg,#33a6d7 0%,#86cfc6 55%,#fbd86a 100%)"></div>
</header>

<section class="about">
  <div class="frame"></div><div class="frame2"></div>
  <div class="art" role="img" aria-label="Illustration of web interface windows and gears" style="left:36px;top:38px;width:324px;height:305px;border-radius:0;background:linear-gradient(135deg,#e7eaec 0%,#9cc3d6 100%)"></div>
  <h2>About <span>Us</span></h2>
  <p>Lorem Ipsum is simply dummy text of the printing and typesetting industry. Lorem Ipsum has been the industry's standard dummy text ever since the 1500s, when an unknown printer took a galley of type and scrambled it to make a type specimen book. It has survived not only five.</p>
  <div class="btn-outline">Read More</div>
  <div class="thumb" role="img" aria-label="Illustration of a developer workspace" style="left:440px;background:linear-gradient(135deg,#2bb3c9,#1e8aa8)"></div>
  <div class="thumb" role="img" aria-label="Illustration of a laptop on a desk" style="left:625px;background:linear-gradient(135deg,#e9eef2,#b8c7d2)"></div>
  <div class="thumb" role="img" aria-label="Illustration of a team working on screens" style="left:810px;background:linear-gradient(135deg,#29b0c4,#2c7e9b)"></div>
  <div class="slider-arrow" style="left:434px">‹</div>
  <div class="slider-arrow" style="left:982px">›</div>
</section>

<section class="goal">
  <h2 style="left:174px;top:1056px">Our <span>Company's Goal</span></h2>
  <p class="block-text" style="left:174px;top:1114px;width:410px">Make organization's communication smooth and healthy with transparency and efficiency for works and tasks in all levels with our workflow tool.</p>
  <div class="art" role="img" aria-label="Line illustration of analytics charts, a target and a person at a screen" style="left:622px;top:1014px;width:425px;height:185px;background:linear-gradient(120deg,#dbeef8 0%,#8fc7e6 60%,#cadf82 100%)"></div>
</section>

<div class="divider"></div>

<section class="mission">
  <div class="art" role="img" aria-label="Illustration of interlocking gears with team members" style="left:192px;top:1292px;width:342px;height:230px;background:linear-gradient(135deg,#c9cdd1 0%,#e9e5c9 60%,#fee18a 100%)"></div>
  <h2 style="left:610px;top:1336px">Our <span>Mission</span></h2>
  <p class="block-text" style="left:612px;top:1392px;width:420px">Our mission is to achieve business goals with customers. We work together to identify the goals for your company, guides your strategy and bring the technology answers which best fit to achieve the goals.</p>
</section>

<section class="services">
  <h2>What <span>We Do</span></h2>

  <article class="card" style="top:139px;height:380px">
    <div class="art" role="img" aria-label="Illustration of a laptop with code surrounded by development icons" style="left:43px;top:35px;width:306px;height:306px;border-radius:50%;background:linear-gradient(160deg,#dbeef8 0%,#33a6d7 55%,#f08a7a 100%)"></div>
    <div class="svc-icon" style="left:475px;top:16px"></div>
    <h3 class="svc-title" style="left:546px;top:22px">System Development &amp;<br>Implementation Service</h3>
    <p class="svc-text" style="left:475px;top:96px;width:500px">We will provide end-to-end PM service with experienced PM. Our service is not only "managing" but "leading" to bring success to achieve the goal.</p>
    <p class="svc-text" style="left:475px;top:148px">We have a workflow tool "velmora"</p>
    <ul class="ticks" style="left:475px;top:180px;width:520px">
      <li>Very simple end-user configurable workflow for any companyprocesses(Targeting small-med size company)</li>
      <li>Graphical &amp; fun features for startup users</li>
      <li>Simple and easy task control with quillbox e-mail look &amp; feel</li>
      <li>Non charged skill up guidance</li>
      <li>Additional features with &amp; Multiple delegation &amp; Clear status for each owner &amp; Task owner management console with due date reminders &amp; reporting</li>
    </ul>
  </article>

  <article class="card" style="top:556px;height:381px">
    <div class="svc-icon" style="left:26px;top:122px"></div>
    <h3 class="svc-title" style="left:98px;top:128px">Project Management(PM)<br>Service</h3>
    <p class="svc-text" style="left:26px;top:198px;width:500px">We will provide end-to-end PM service with experienced PM.Our service is not only "managing" but "leading" to bring success to achieve the goal.</p>
    <div class="art" role="img" aria-label="Top-down illustration of two people working at a round desk" style="left:628px;top:10px;width:362px;height:362px;border-radius:50%;background:linear-gradient(135deg,#33b8a4 0%,#dbeef8 45%,#0255a3 100%)"></div>
  </article>

  <article class="card" style="top:972px;height:379px">
    <div class="art" role="img" aria-label="Illustration of a monitor with communication and web icons" style="left:22px;top:74px;width:360px;height:240px;background:linear-gradient(135deg,#f08a7a 0%,#e9eef2 50%,#33a6d7 100%)"></div>
    <div class="svc-icon" style="left:465px;top:124px"></div>
    <h3 class="svc-title" style="left:532px;top:142px">Consultation Service</h3>
    <p class="svc-text" style="left:474px;top:204px;width:500px">Consulting services to a wide range of fields such as creating business strategy, business process Kaizen, IT system consultation and change management.</p>
  </article>
</section>

<footer class="footer">
  <h3 style="left:87px;top:28px">Contact Information</h3>
  <div class="info" style="top:62px">
    <svg width="14" height="14" viewBox="0 0 24 24"><path d="M6.6 10.8a15 15 0 006.6 6.6l2.2-2.2c.3-.3.7-.4 1-.2 1.1.4 2.3.6 3.6.6.6 0 1 .4 1 1V20c0 .6-.4 1-1 1C10.6 21 3 13.4 3 4c0-.6.4-1 1-1h3.5c.6 0 1 .4 1 1 0 1.3.2 2.5.6 3.6.1.3 0 .7-.2 1z" fill="#fff"/></svg>
    <span>555-014-2208</span>
  </div>
  <div class="info" style="top:104px">
    <svg width="14" height="14" viewBox="0 0 24 24"><rect x="2" y="5" width="20" height="14" rx="2" fill="#fff"/><path d="M3 6l9 7 9-7" fill="none" stroke="#6b7d12" stroke-width="2"/></svg>
    <span>hello@corvane.example</span>
  </div>
  <div class="info" style="top:142px">
    <svg width="14" height="16" viewBox="0 0 24 28"><path d="M12 1a9 9 0 00-9 9c0 7 9 17 9 17s9-10 9-17a9 9 0 00-9-9z" fill="#fff"/><circle cx="12" cy="10" r="3.5" fill="#6b7d12"/></svg>
    <span>Lorem Ipsum is simply dummy text of the</span>
  </div>
  <div class="vline"></div>

  <h3 style="left:497px;top:28px">Contact Us</h3>
  <div class="field" style="left:497px;top:60px;width:300px">Name *<br>&nbsp;</div>
  <div class="field" style="left:813px;top:72px;width:300px">Phone No</div>
  <div class="field" style="left:497px;top:106px;width:616px">Email Id</div>
  <div class="field" style="left:497px;top:140px;width:616px;height:44px">Message</div>
  <div class="send">Send Message</div>
</footer>
<div class="copyright">© 2018. Corvane. All Rights Reserved.</div>

</body>
</html>
```